Lorvik.no is a new website about pedagogical entrepreneurship. It's main target group is teachers. The Fjellmark Bureau for Digital Schooling and the Halvstad Agency for Classroom Affairs are leading the project.

The web page is meant to show examples of how different methods of entrepreneurship can be used pedagogical in a learning environment. The page will also support the user with examples of different teaching programs and other examples of best practice.

Pedagogical entrepreneurship is not about business and men in suits. It's a method for learning. The focus in the design should be on school, education and new ways of learning.

The final product should be motivating and engaging, but at the same time governmental and serious. We are not looking for something "flashy" and corporate-looking, but a moderate, task-focused and clean design that state quality.

We need designs for three pages:
1 - frontpage
2 - subpage ("Metoder og undervisningsopplegg")
3 - subpage ("Tavle-KOMP i Brekkvoll")

The interaction design for these three pages will be uploaded as an attachment.

We would like you to find inspiration in the following websites:
- www.skaperlund.no
- www.guldrim.no
- www.brambelquest.com
- www.tuv.no
(more will be added)

Please use the attached logo, and feel free to use this as an inspiration for the rest of the design.

Reason: We are awaiting improved designs from some designers, and need to extend the deadline a couple of days.

Target Market(s)

Teachers

Industry/Entity Type

Education

Requirements
Must have
• * Header with: Logo. Main navigation. Utility navigation. Search box.
* Footer
Should not have
• Images of men in suits.
Very strong graphical elements that stands out too much (we want it clean).

```html
<!DOCTYPE html>
<html lang="en">
<head>
<meta charset="utf-8">
<title>Lorvik.no – Methods</title>
<link rel="stylesheet" href="https://fonts.googleapis.com/css2?family=Open+Sans:wght@400;600;700&display=swap">
<style>
  :root{
    --page:#ffffff;
    --stage-top:#d9dfe3;
    --stage-mid:#8fb0c2;
    --stage-bottom:#1f5d7f;
    --foot-top:#5d93ad;
    --foot-bottom:#0b4768;
    --panel:#f5f5f5;
    --panel-edge:#e6e6e6;
    --brand:#2a8fd0;
    --brand-dark:#1b5877;
    --nav-grey:#c9c9c9;
    --sub-text:#2a84c6;
    --intro:#6f8db4;
    --row:#c6c6c6;
    --util:#6d6d6d;
    --foot-link:#a6dbf5;
  }
  *{box-sizing:border-box;margin:0;padding:0}
  html,body{width:1200px;height:1099px;overflow:hidden;background:var(--page);font-family:"Open Sans",Arial,sans-serif}
  .stage{position:absolute;left:52px;top:52px;width:1097px;height:1001px;
    background:linear-gradient(180deg,var(--stage-top) 0%,#b9c8d1 25%,var(--stage-mid) 50%,#4f84a1 75%,var(--stage-bottom) 100%)}
  .footer{position:absolute;left:0;top:867px;width:1097px;height:134px;
    background:linear-gradient(180deg,var(--foot-top),var(--foot-bottom));border-top:1px solid #7fa9be}

  .brand{position:absolute;left:68px;top:30px;display:flex;align-items:center;gap:26px}
  .brand-dot{width:58px;height:58px;border-radius:50%;background:var(--brand)}
  .brand-name{font-weight:700;font-size:54px;line-height:1;color:var(--brand);letter-spacing:-1px}
  .brand-tagline{position:absolute;left:161px;top:86px;font-size:10px;font-weight:600;color:#fff;white-space:nowrap}

  .side-panel{position:absolute;left:69px;top:178px;width:380px;height:607px;border-radius:22px;
    background:linear-gradient(180deg,var(--panel),var(--panel-edge));box-shadow:0 6px 18px rgba(0,0,0,.25)}
  .main-nav a{position:absolute;left:20px;width:270px;height:52px;padding:8px 0 0 59px;
    font-size:13px;line-height:17px;text-transform:uppercase;color:#fff;text-decoration:none;
    background:var(--nav-grey);box-shadow:0 2px 3px rgba(0,0,0,.2)}
  .main-nav a.active{background:var(--brand-dark)}
  .method-list a{position:absolute;left:118px;width:170px;height:26px;padding-left:10px;
    font-size:9px;font-weight:600;line-height:26px;text-transform:uppercase;color:var(--sub-text);
    text-decoration:none;white-space:nowrap;background:#fff;box-shadow:0 2px 3px rgba(0,0,0,.18)}

  .content-panel{position:absolute;left:357px;top:139px;width:709px;height:658px;border-radius:22px;
    background:linear-gradient(180deg,#fafafa,var(--panel-edge));box-shadow:0 8px 22px rgba(0,0,0,.3)}
  .utility-nav{position:absolute;left:50px;top:21px;display:flex;gap:21px}
  .utility-nav a{font-size:11px;color:var(--util);text-decoration:underline}
  .search{position:absolute;left:492px;top:20px;width:170px;height:21px;border:1px solid #c8c8c8;background:#fff}
  .search-text{position:absolute;left:7px;top:2px;font-size:10px;color:#888}
  .search-btn{position:absolute;right:0;top:0;width:22px;height:19px;background:#d4d4d4}
  .page-title{position:absolute;left:50px;top:67px;font-size:19px;font-weight:700;color:var(--brand)}
  .intro{position:absolute;left:50px;top:103px;width:172px;font-size:12px;line-height:16.5px;color:var(--intro)}

  .plans{position:absolute;left:50px;top:263px;width:612px}
  .plans-head{height:22px;padding-left:6px;font-size:11px;font-weight:600;line-height:22px;color:#fff;text-transform:uppercase;
    background:linear-gradient(180deg,#4d83a2,#1d587a)}
  .filters{position:relative;height:32px}
  .filters .label{position:absolute;left:7px;top:8px;font-size:12px;color:#777}
  .select{position:absolute;top:6px;height:20px;border:1px solid #c5c5c5;background:#e6e6e6;font-size:11.5px;color:#777;padding:2px 0 0 4px}
  .select::after{content:"";position:absolute;right:0;top:0;width:20px;height:18px;background:#b7b7b7}
  .select i{position:absolute;right:6px;top:7px;border:4px solid transparent;border-top:5px solid #fff;z-index:1}
  .row{position:absolute;left:0;width:612px;height:26px;background:var(--row);color:#fff;font-size:12px;line-height:26px}
  .row span{position:absolute}
  .c-title{left:7px}.c-level{left:199px}.c-time{left:339px}.c-subject{left:450px}
  .back{position:absolute;left:54px;top:627px;font-size:12px;color:var(--intro);text-decoration:none}

  .foot-dot{position:absolute;left:96px;top:16px;width:50px;height:50px;border-radius:50%;background:#fff}
  .foot-col{position:absolute;top:18px;font-size:8.5px;line-height:15px}
  .foot-col h4{font-size:8.5px;font-weight:700;color:#fff}
  .foot-col p{color:var(--foot-link);margin-bottom:10px;white-space:nowrap}
  .foot-col b{color:#fff}
</style>
</head>
<body>
<div class="stage">
  <header>
    <div class="brand"><span class="brand-dot"></span><span class="brand-name">Lorvik</span></div>
    <div class="brand-tagline">Entreprenerielle metoder i undervisningen</div>
  </header>

  <aside class="side-panel">
    <nav class="main-nav">
      <a style="top:21px">What is pedagogical<br>entrepreneurship</a>
      <a class="active" style="top:81px">Methods and<br>teaching plans</a>
      <a style="top:140px">Good examples/<br>best pratice</a>
    </nav>
    <nav class="method-list">
      <a style="top:232px">Story line</a>
      <a style="top:267px">Elevbedrift /ungdomsbedrift</a>
      <a style="top:302px">Problembasert laering</a>
      <a style="top:337px">Real</a>
      <a style="top:372px">Uteskole-pedagogikk</a>
      <a style="top:407px">Partnerskap</a>
      <a style="top:442px">Prosjektarbeid</a>
      <a style="top:477px">Kreative ekskursjoner</a>
      <a style="top:512px">Gründercamp</a>
    </nav>
  </aside>

  <main class="content-panel">
    <nav class="utility-nav">
      <a>best pratice school</a><a>Try lorvikmeter</a><a>about&nbsp; lorvik.no</a>
    </nav>
    <div class="search"><span class="search-text">search ...</span><span class="search-btn"></span></div>
    <h1 class="page-title">METHODS</h1>
    <p class="intro">text about the methods and how they can be used. Also an intro to how teachers can find teaching resources</p>

    <section class="plans">
      <div class="plans-head">Find teaching plans</div>
      <div class="filters">
        <span class="label">Title</span>
        <span class="select" style="left:199px;width:70px">Level<i></i></span>
        <span class="select" style="left:339px;width:70px">Time<i></i></span>
        <span class="select" style="left:449px;width:156px">Subject<i></i></span>
      </div>
      <div class="row" style="top:61px"><span class="c-title">Title</span><span class="c-level">5-7 level</span><span class="c-time">2 weeks</span><span class="c-subject">Norwegian, Maths, English</span></div>
      <div class="row" style="top:90px"><span class="c-title">Title</span><span class="c-level">5-7 level</span><span class="c-time">2 weeks</span><span class="c-subject">Norwegian, Maths, English</span></div>
      <div class="row" style="top:122px"><span class="c-title">Title</span><span class="c-level">5-7 level</span><span class="c-time">2 weeks</span><span class="c-subject">Norwegian, Maths, English</span></div>
      <div class="row" style="top:155px"><span class="c-title">Title</span><span class="c-level">5-7 level</span><span class="c-time">2 weeks</span><span class="c-subject">Norwegian, Maths, English</span></div>
      <div class="row" style="top:189px"><span class="c-title">Title</span><span class="c-level">5-7 level</span><span class="c-time">2 weeks</span><span class="c-subject">Norwegian, Maths, English</span></div>
      <div class="row" style="top:223px"><span class="c-title">Title</span><span class="c-level">5-7 level</span><span class="c-time">2 weeks</span><span class="c-subject">Norwegian, Maths, English</span></div>
      <div class="row" style="top:255px"><span class="c-title">Title</span><span class="c-level">5-7 level</span><span class="c-time">2 weeks</span><span class="c-subject">Norwegian, Maths, English</span></div>
      <div class="row" style="top:289px"><span class="c-title">Title</span><span class="c-level">5-7 level</span><span class="c-time">2 weeks</span><span class="c-subject">Norwegian, Maths, English</span></div>
    </section>
    <a class="back">&lt; back</a>
  </main>

  <footer class="footer">
    <span class="foot-dot"></span>
    <div class="foot-col" style="left:211px">
      <h4>Pedagogical entrepreneurship</h4>
      <p>What is pedagogical entrepreneurship? | Science | Best pratice schools | Lorvikmeteret | About lorvik.no</p>
      <h4>Gode eksempler</h4>
      <p>Tavle-KOMP at Brekkvoll school | Tavle-KOMP at Brekkvoll school | Tavle-KOMP at Brekkvoll school | more...</p>
    </div>
    <div class="foot-col" style="left:710px">
      <h4>Teaching Plans</h4>
      <p>Lorem ipsum | Lorem ipsum | Lorem ipsum | Lorem ipsum | more...</p>
      <h4>Methods</h4>
      <p>Story line | <b>REAL</b> | Café-pedagogikk | more...</p>
    </div>
  </footer>
</div>
</body>
</html>
```